Option Sheet

We need a one page option sheet with a left to right reading of the five options. It should be a one sheet, multiple colors and definitive separations between options This is used in a sales consultation. Backround or colors not in option need to have the follow RGB value (5 red, 20 green, 63 blue)

We added a smaller text file, please change that point

Target Market(s)

Divorce

Industry/Entity Type

Legal

Requirements
Must have
• 1) All five options left to right
• 2)language included in sheet

```html
<!DOCTYPE html>
<html lang="en">
<head>
<meta charset="UTF-8">
<title>Five Options – Divorce</title>
<link href="https://fonts.googleapis.com/css2?family=Source+Sans+3:ital,wght@0,300;0,400;0,700;1,300;1,400&display=swap" rel="stylesheet">
<style>
  :root {
    --navy: rgb(5, 20, 63);
    --white: #ffffff;
    --ink: #3a3a3a;
    --muted: #5a5a5a;
    --rule: #ececec;
    --orange: #f9502b;
    --pink: #d64f9b;
    --purple: #4a3894;
    --lime: #7fc21f;
    --green: #039640;
  }
  * { box-sizing: border-box; margin: 0; padding: 0; }
  html, body {
    width: 1200px; height: 680px; overflow: hidden;
    background: var(--navy);
    font-family: "Source Sans 3", "Myriad Pro", sans-serif;
  }
  .sheet { position: relative; width: 1200px; height: 680px; }
  .sheet-title {
    position: absolute; top: 26px; left: 0; width: 100%;
    text-align: center; color: var(--white);
  }
  .sheet-kicker { font-size: 29px; font-weight: 400; letter-spacing: 1px; line-height: 36px; }
  .sheet-headline { font-size: 62px; font-weight: 700; letter-spacing: 1px; line-height: 66px; margin-top: 2px; }

  .options {
    position: absolute; top: 158px; left: 16px;
    display: flex; gap: 4.6px; align-items: flex-start;
  }
  .option { width: 230px; background: var(--white); }
  .option--nothing { --accent: var(--orange); height: 386px; }
  .option--counseling { --accent: var(--pink); height: 446px; }
  .option--diy { --accent: var(--purple); height: 473px; }
  .option--limited { --accent: var(--lime); height: 490px; }
  .option--hire { --accent: var(--green); height: 506px; }

  .option-header {
    height: 80px; background: var(--accent); color: var(--white);
    display: flex; flex-direction: column; align-items: center; justify-content: center;
    text-align: center;
  }
  .option-number { font-size: 12.5px; font-style: italic; font-weight: 300; line-height: 15px; }
  .option-name { font-size: 28px; font-weight: 700; line-height: 30px; letter-spacing: -0.5px; margin-top: 2px; }
  .option-name--two-line { font-size: 27px; line-height: 23px; margin-top: 1px; }

  .option-body { padding: 0 16px 0 20px; }
  .pros { height: 126px; padding-top: 24px; }
  .option--hire .pros { height: 246px; }
  .divider { height: 1px; background: var(--rule); margin-right: 6px; }
  .cons { padding-top: 23px; }
  .group-label { font-size: 17.5px; font-weight: 400; color: var(--ink); line-height: 20px; margin-bottom: 10px; }

  .point-list { list-style: none; }
  .point {
    position: relative; padding-left: 27px;
    font-size: 14.6px; font-style: italic; font-weight: 300; color: var(--muted);
    line-height: 15px; margin-bottom: 15px; letter-spacing: -0.2px;
  }
  .point .tick { position: absolute; left: 0; top: 2px; width: 13px; height: 11px; }
</style>
</head>
<body>
<main class="sheet">
  <header class="sheet-title">
    <p class="sheet-kicker">Five Options</p>
    <h1 class="sheet-headline">DIVORCE</h1>
  </header>

  <svg width="0" height="0" style="position:absolute">
    <defs>
      <symbol id="tick" viewBox="0 0 13 11">
        <path d="M1.2 5.8 L4.8 9.2 L11.8 1.6" fill="none" stroke="currentColor" stroke-width="2.4" stroke-linecap="round" stroke-linejoin="round"/>
      </symbol>
    </defs>
  </svg>

  <section class="options">
    <article class="option option--nothing">
      <div class="option-header"><span class="option-number">option #1</span><h2 class="option-name">Do Nothing</h2></div>
      <div class="option-body">
        <div class="pros">
          <h3 class="group-label">Advantages:</h3>
          <ul class="point-list">
            <li class="point"><svg class="tick" style="color:var(--accent)"><use href="#tick"/></svg>Stay married</li>
            <li class="point"><svg class="tick" style="color:var(--accent)"><use href="#tick"/></svg>No life Changes</li>
          </ul>
        </div>
        <div class="divider"></div>
        <div class="cons">
          <h3 class="group-label">Disadvantages:</h3>
          <ul class="point-list">
            <li class="point"><svg class="tick" style="color:var(--accent)"><use href="#tick"/></svg>Remainunhappy, depressed, anxious</li>
            <li class="point"><svg class="tick" style="color:var(--accent)"><use href="#tick"/></svg>Money and assets may disappear</li>
            <li class="point"><svg class="tick" style="color:var(--accent)"><use href="#tick"/></svg>What is going to change?</li>
          </ul>
        </div>
      </div>
    </article>

    <article class="option option--counseling">
      <div class="option-header"><span class="option-number">option #2</span><h2 class="option-name">Go to Counseling</h2></div>
      <div class="option-body">
        <div class="pros">
          <h3 class="group-label">Advantages:</h3>
          <ul class="point-list">
            <li class="point"><svg class="tick" style="color:var(--accent)"><use href="#tick"/></svg>Reconcile marriage</li>
            <li class="point"><svg class="tick" style="color:var(--accent)"><use href="#tick"/></svg>Help make a better life</li>
          </ul>
        </div>
        <div class="divider"></div>
        <div class="cons">
          <h3 class="group-label">Disadvantages:</h3>
          <ul class="point-list">
            <li class="point"><svg class="tick" style="color:var(--accent)"><use href="#tick"/></svg>Past issues are highlighted and may drudge up old wounds</li>
            <li class="point"><svg class="tick" style="color:var(--accent)"><use href="#tick"/></svg>It may just clarify the reasons you need to separate and/or divorce</li>
            <li class="point"><svg class="tick" style="color:var(--accent)"><use href="#tick"/></svg>Both parties must be invested and willing to participate</li>
          </ul>
        </div>
      </div>
    </article>

    <article class="option option--diy">
      <div class="option-header"><span class="option-number">option #3</span><h2 class="option-name">Do it Yourself</h2></div>
      <div class="option-body">
        <div class="pros">
          <h3 class="group-label">Advantages:</h3>
          <ul class="point-list">
            <li class="point"><svg class="tick" style="color:var(--accent)"><use href="#tick"/></svg>No attorney fees</li>
            <li class="point"><svg class="tick" style="color:var(--accent)"><use href="#tick"/></svg>You are youron attorney</li>
          </ul>
        </div>
        <div class="divider"></div>
        <div class="cons">
          <h3 class="group-label">Disadvantages:</h3>
          <ul class="point-list">
            <li class="point"><svg class="tick" style="color:var(--accent)"><use href="#tick"/></svg>People often find that what is “fair,” may in fact, not be truly fair</li>
            <li class="point"><svg class="tick" style="color:var(--accent)"><use href="#tick"/></svg>Often times, people do not know the risks</li>
            <li class="point"><svg class="tick" style="color:var(--accent)"><use href="#tick"/></svg>Complicated legal system within intrigue rules</li>
            <li class="point"><svg class="tick" style="color:var(--accent)"><use href="#tick"/></svg>Unsure how to complete the necessary paperwork and meet the deadlines</li>
          </ul>
        </div>
      </div>
    </article>

    <article class="option option--limited">
      <div class="option-header"><span class="option-number">option #4</span><h2 class="option-name option-name--two-line">Limited<br>Representation</h2></div>
      <div class="option-body">
        <div class="pros">
          <h3 class="group-label">Advantages:</h3>
          <ul class="point-list">
            <li class="point"><svg class="tick" style="color:var(--accent)"><use href="#tick"/></svg>Balance between going alone and our limited involvement in the case</li>
          </ul>
        </div>
        <div class="divider"></div>
        <div class="cons">
          <h3 class="group-label">Disadvantages:</h3>
          <ul class="point-list">
            <li class="point"><svg class="tick" style="color:var(--accent)"><use href="#tick"/></svg>Our terms may not benefit from our legal knowledge</li>
            <li class="point"><svg class="tick" style="color:var(--accent)"><use href="#tick"/></svg>The legal consequences of your legal documents will not be explained to you so that you can formulate a plan for handling the rest of your case.</li>
            <li class="point"><svg class="tick" style="color:var(--accent)"><use href="#tick"/></svg>Your spouse or other parties may cause your legal fees to increase significantly without action on your part</li>
          </ul>
        </div>
      </div>
    </article>

    <article class="option option--hire">
      <div class="option-header"><span class="option-number">option #5</span><h2 class="option-name">Hire Us</h2></div>
      <div class="option-body">
        <div class="pros">
          <h3 class="group-label">Advantages:</h3>
          <ul class="point-list">
            <li class="point"><svg class="tick" style="color:var(--accent)"><use href="#tick"/></svg>Gain the full benefits of our experience</li>
            <li class="point"><svg class="tick" style="color:var(--accent)"><use href="#tick"/></svg>Have a team of Family Law focus attorneys</li>
            <li class="point"><svg class="tick" style="color:var(--accent)"><use href="#tick"/></svg>Often saves you or makes you money in the long run</li>
            <li class="point"><svg class="tick" style="color:var(--accent)"><use href="#tick"/></svg>Save you time, energy and stress</li>
          </ul>
        </div>
        <div class="divider"></div>
        <div class="cons">
          <h3 class="group-label">Disadvantages:</h3>
          <ul class="point-list">
            <li class="point"><svg class="tick" style="color:var(--accent)"><use href="#tick"/></svg>Remainunhappy, depressed, anxious</li>
            <li class="point"><svg class="tick" style="color:var(--accent)"><use href="#tick"/></svg>Money and assets may disappear</li>
            <li class="point"><svg class="tick" style="color:var(--accent)"><use href="#tick"/></svg>What is going to change?</li>
          </ul>
        </div>
      </div>
    </article>
  </section>
</main>
</body>
</html>
```